Classy business card for accounting firm

We're looking for a new business card for our accounting firm. Our logo was designed by Brandolith, so all of the design info we would like to use has been provided. The specific font provided isn't required to be used.

We want the card to look classy and elegent. Probably more minimalistic, but still with some pops of color.

The options we would like to include on the card are as follows:
1. Main office phone line
2. Direct phone line
3. Email address
4. Website URL
5. Name
6. Title (CEO, President, etc.)
7. Firm Address

The design and card should be double sided!!! The drop down box in the project brief for some reason is defaulting to single sided. Not sure why this is happening.

Thanks!

Contact Information for Business Card

The options we would like to include on the card are as follows: 1. Main office phone line 2. Direct phone line 3. Email address 4. Website URL 5. Name 6. Title (CEO, President, etc.) 7. Firm Address

Requirements
Must have
• Card must be double sided.

```html
<!DOCTYPE html>
<html lang="en">
<head>
<meta charset="utf-8">
<title>Ledgerline Partners – Business Card</title>
<link rel="stylesheet" href="https://fonts.googleapis.com/css2?family=Open+Sans:wght@400;600;700;800&display=swap">
<style>
  :root{
    --stage:#222223;
    --card:#232326;
    --card-deep:#1a1a1c;
    --orange:#f47b20;
    --green:#a4c639;
    --grey:#8a8a8e;
    --white:#ffffff;
  }
  *{box-sizing:border-box;margin:0;padding:0}
  html,body{width:1200px;height:780px;overflow:hidden;background:var(--stage)}
  body{position:relative;font-family:"Open Sans",Arial,sans-serif;color:var(--white)}

  .card{
    position:absolute;width:540px;height:309px;border-radius:18px;
    background:var(--card);overflow:hidden;
    border-bottom:4px solid var(--orange);border-left:2px solid var(--orange);
    box-shadow:0 14px 30px rgba(0,0,0,.55);
  }
  .card--back{left:60px;top:70px}
  .card--front{left:600px;top:400px}

  /* back side: pattern area rendered as a soft silver-to-black field */
  .pattern-field{
    position:absolute;inset:0;
    background:
      radial-gradient(ellipse 70% 60% at 85% 0%,rgba(200,200,204,.55) 0%,rgba(120,120,124,.3) 40%,rgba(0,0,0,0) 75%),
      linear-gradient(180deg,#1f1f21 0%,#161618 100%);
  }
  .brand{position:absolute;display:flex;align-items:center;gap:14px;white-space:nowrap}
  .brand__square{width:26px;height:26px;background:var(--orange);flex:none}
  .brand__text{display:flex;flex-direction:column;align-items:flex-start}
  .brand__name{font-weight:600;font-size:22px;letter-spacing:3px;color:var(--grey);text-transform:uppercase;line-height:1.1;white-space:nowrap}
  .brand__tagline{display:flex;align-items:center;gap:8px;margin-top:5px;font-weight:600;font-size:9px;letter-spacing:2.5px;color:var(--grey);text-transform:uppercase;white-space:nowrap}
  .brand__rule{height:1px;width:42px;background:var(--green);flex:none}
  .card--back .brand{left:50%;top:50%;transform:translate(-50%,-50%)}

  /* front side */
  .decor-field{
    position:absolute;right:0;top:70px;width:210px;height:239px;
    background:linear-gradient(180deg,#4a4a4e 0%,#1b1b1d 45%,#111113 100%);
    clip-path:polygon(25% 0,80% 0,100% 30%,100% 100%,30% 100%,0 50%);
  }
  .identity{position:absolute;right:0;top:16px;display:flex;align-items:stretch}
  .identity__text{text-align:right;padding-right:12px}
  .identity__name{font-weight:800;font-size:27px;line-height:1.05;white-space:nowrap}
  .identity__first{color:var(--orange)}
  .identity__last{color:var(--green)}
  .identity__title{font-size:13px;font-weight:600;color:var(--white);margin-top:2px}
  .identity__tab{width:18px;background:var(--orange)}
  .card--front .brand{left:30px;top:86px}
  .card--front .brand__name{font-size:19px}

  .address{position:absolute;left:58px;top:168px;font-size:13px;line-height:1.4;font-style:normal}
  .contacts{position:absolute;left:40px;top:218px;list-style:none;font-size:13px;line-height:1}
  .contacts li{display:flex;align-items:center;gap:9px;height:19px}
  .contacts svg{width:12px;height:12px;flex:none}
</style>
</head>
<body>

<section class="card card--back" aria-label="Card back">
  <div class="pattern-field" role="img" aria-label="Repeating brand symbol pattern fading from silver to black"></div>
  <div class="brand">
    <span class="brand__square"></span>
    <div class="brand__text">
      <span class="brand__name">Ledgerline Partners</span>
      <span class="brand__tagline"><span class="brand__rule"></span>Solving tax problems<span class="brand__rule"></span></span>
    </div>
  </div>
</section>

<section class="card card--front" aria-label="Card front">
  <div class="decor-field" role="img" aria-label="Large embossed brand symbol in dark grey"></div>

  <div class="identity">
    <div class="identity__text">
      <p class="identity__name"><span class="identity__first">Mara</span> <span class="identity__last">Kellner</span></p>
      <p class="identity__title">Managing Director</p>
    </div>
    <span class="identity__tab"></span>
  </div>

  <div class="brand">
    <span class="brand__square"></span>
    <div class="brand__text">
      <span class="brand__name">Ledgerline Partners</span>
      <span class="brand__tagline"><span class="brand__rule"></span>Solving tax problems<span class="brand__rule"></span></span>
    </div>
  </div>

  <address class="address">418 Alder Row, Suite 310<br>Halden, TX 75001</address>

  <ul class="contacts">
    <li><svg viewBox="0 0 12 12"><rect x="3" y="0.5" width="6" height="11" rx="1" fill="none" stroke="#a4c639" stroke-width="1.2"/></svg>(555) 214-3861</li>
    <li><svg viewBox="0 0 12 12"><path d="M2 1.5l2.5 0 1 2.5-1.5 1c.6 1.3 1.5 2.2 2.8 2.8l1-1.5 2.5 1v2.5c-5 0-8.3-3.3-8.3-8.3z" fill="#f47b20"/></svg>(555) 214-3800</li>
    <li><svg viewBox="0 0 12 12"><rect x="0.8" y="2.5" width="10.4" height="7.5" fill="none" stroke="#a4c639" stroke-width="1.2"/><path d="M1 3l5 4 5-4" fill="none" stroke="#a4c639" stroke-width="1.2"/></svg>hello@ledgerline.com</li>
    <li><svg viewBox="0 0 12 12"><circle cx="6" cy="6" r="5.2" fill="#f47b20"/><path d="M1 6h10M6 1c-2 2.5-2 7.5 0 10M6 1c2 2.5 2 7.5 0 10" fill="none" stroke="#232326" stroke-width=".8"/></svg>www.ledgerline.com</li>
  </ul>
</section>

</body>
</html>
```